Fabrication and machining company needing printed material designs.

Heron Vessels, Inc. wants to use appealing visuals as well as informative text to tell potential clients about our capabilities in fabrication and machining. We have a new logo to showcase as well as a new website. The use of print media will allow us to leave tangible information with clients, and therefore the design will need to be concise, informative, and visually appealing.

Full Page Flyer (approx. 8.5" x 11"), front and back design. This will be a detailed offering of capabilities and services for our shop.

Half Page Flyer (approx. 5.5" x 8.5"), front and back design. An abbreviated version of the full page flyer, meant to be easily handed out and stored inside a note book.

Bi-fold business card front and back. General offerings of our services. Minimal if any details. Finished size is twice the size of a business card (approx. 4" x 3.5"), once folded in half will be the same size as a standard business card (approx. 2" x 3.5").

Please use www.heronvesselsinc.example for theme ideas. The font used for our logo is ethnocentric, not to be used for all text.

Target Market(s)

Industrial Consumers

Font styles to use
Sans Serif

```html
<!DOCTYPE html>
<html lang="en">
<head>
<meta charset="utf-8">
<title>Heron Vessels, Inc. — Print Collateral</title>
<link rel="stylesheet" href="https://fonts.googleapis.com/css2?family=Montserrat:wght@400;500;600;700;800&family=Orbitron:wght@700;800;900&display=swap">
<style>
:root{
  --orange:#f26b21;
  --orange-dark:#d9561a;
  --black:#141414;
  --charcoal:#232323;
  --grey:#e9e9e9;
  --grey-mid:#bdbdbd;
  --text:#2a2a2a;
  --white:#ffffff;
  --stage:#ebe8e3;
  --body:'Montserrat', Arial, sans-serif;
  --display:'Orbitron', 'Montserrat', sans-serif;
}
*{box-sizing:border-box;margin:0;padding:0}
html,body{width:1200px;height:3000px;overflow:hidden}
body{background:var(--stage);font-family:var(--body);color:var(--text)}
.sheet-set{width:1200px;height:3000px;display:flex;flex-direction:column;justify-content:space-evenly;align-items:center;padding:60px 0}
.row{display:flex;gap:60px;align-items:flex-start}
.item{display:flex;flex-direction:column;align-items:center;gap:18px}
.size-label{font-size:15px;font-weight:600;letter-spacing:1px;color:#555;text-transform:uppercase}
.page{background:var(--white);box-shadow:0 8px 24px rgba(0,0,0,.18);position:relative;overflow:hidden;display:flex;flex-direction:column}

/* brand */
.brand{display:flex;align-items:center;gap:8px;font-family:var(--body);font-weight:800;color:var(--black);font-size:13px;letter-spacing:.5px}
.brand-mark{width:20px;height:20px;background:var(--black)}
.brand.on-dark{color:var(--white)}
.brand.on-dark .brand-mark{background:var(--white)}

.photo{background:linear-gradient(135deg,#2b2b2b 0%,#5a3a22 45%,#c46a2a 60%,#1a1a1a 100%)}
.photo-cool{background:linear-gradient(135deg,#1c2630 0%,#3d4c58 50%,#141414 100%)}
.photo-circle{border-radius:50%;border:3px solid var(--white);background:radial-gradient(circle at 40% 40%,#f0a05a,#6a3415 55%,#1a1a1a)}

.headline{font-family:var(--display);font-weight:900;line-height:1.05;letter-spacing:1px;text-transform:uppercase}
.headline .white{color:var(--white)}
.headline .orange{color:var(--orange)}

.bar{background:var(--orange);color:var(--white);font-weight:800;text-transform:uppercase;letter-spacing:1.5px}
.section-title{color:var(--orange);font-weight:800;text-transform:uppercase;letter-spacing:.5px}
.list{list-style:none}
.list li{position:relative;padding-left:9px}
.list li::before{content:"";position:absolute;left:0;top:.45em;width:4px;height:4px;background:var(--orange)}
.arrow-list{list-style:none}
.arrow-list li{display:flex;align-items:center;gap:6px}
.arrow-list svg{flex:none}
.footer{background:var(--black);color:var(--white);display:flex;justify-content:space-between;align-items:center}
.footer .phone{color:var(--orange);font-weight:800}

/* full page */
.full{width:500px;height:647px}
.full .top{height:62px;display:flex;align-items:center;padding:0 22px}
.full .hero{height:200px;position:relative;background:var(--black)}
.full .hero .photo{position:absolute;right:0;top:0;width:62%;height:100%}
.full .hero .headline{position:absolute;left:22px;top:30px;font-size:25px}
.full .hero .photo-circle{position:absolute;left:40px;bottom:-28px;width:92px;height:92px}
.full .cap-bar{height:30px;margin-left:170px;display:flex;align-items:center;padding-left:18px;font-size:15px}
.full .body{flex:1;display:grid;grid-template-columns:1fr 1fr 150px;gap:12px;padding:20px 18px 12px}
.full .col .block{margin-bottom:9px}
.full .section-title{font-size:8.5px;margin-bottom:2px}
.full .list{font-size:7px;line-height:1.45}
.side-box{background:var(--grey);padding:10px}
.side-box .bar{font-size:8px;padding:4px 6px;margin-bottom:6px}
.side-box .list{font-size:7px;line-height:1.7}
.full .footer{height:48px;padding:0 22px;font-size:9px}
.full .footer .phone{font-size:13px}

/* full back */
.full .back-hero{height:210px}
.full .product{flex:1;display:grid;grid-template-columns:1fr 1fr;gap:16px;padding:20px 22px}
.full .product h3{font-size:13px;margin-bottom:8px}
.full .arrow-list{font-size:8.5px;line-height:2;font-weight:600}
.thumbs{display:grid;grid-template-columns:1fr 1fr;gap:6px}
.thumbs div{height:62px}
.full .closing{height:120px;background:var(--orange);padding:20px 22px;display:flex;flex-direction:column;justify-content:center}
.full .closing .headline{font-size:22px}
.closing .headline .dark{color:var(--black)}

/* half page */
.half{width:420px;height:650px}
.half .top{height:58px;display:flex;align-items:center;padding:0 20px}
.half .hero{height:190px;position:relative;background:var(--black)}
.half .hero .photo{position:absolute;right:0;top:0;width:58%;height:100%}
.half .hero .headline{position:absolute;left:20px;top:30px;font-size:21px}
.half .hero .photo-circle{position:absolute;left:34px;bottom:-26px;width:84px;height:84px}
.half .cap-bar{height:28px;margin-left:140px;display:flex;align-items:center;padding-left:16px;font-size:13px}
.half .body{flex:1;display:grid;grid-template-columns:1fr 1fr;gap:14px;padding:24px 20px 12px}
.half .section-title{font-size:9px;margin-bottom:3px}
.half .list{font-size:8px;line-height:1.55}
.half .block{margin-bottom:10px}
.half .footer{height:50px;padding:0 20px;font-size:8.5px}
.half .footer .phone{font-size:12px}
.half .back-hero{height:200px}
.half .product{flex:1;padding:20px;display:grid;grid-template-columns:1fr 1fr;gap:14px}
.half .product h3{font-size:12px;margin-bottom:8px}
.half .arrow-list{font-size:8.5px;line-height:2;font-weight:600}
.half .thumbs div{height:70px}
.half .closing{height:120px;background:var(--orange);padding:18px 20px;display:flex;flex-direction:column;justify-content:center}
.half .closing .headline{font-size:19px}

/* business card (open, folded across middle) */
.card{width:440px;height:500px;flex-direction:row}
.card .panel{flex:1;position:relative;display:flex;flex-direction:column}
.card .panel + .panel{border-left:1px solid #ddd}
.card .dark-panel{background:var(--black);color:var(--white);justify-content:center;align-items:center;gap:14px;padding:20px}
.card .dark-panel .brand{font-size:13px}
.card .dark-panel .tag{font-size:8px;letter-spacing:2px;color:var(--grey-mid);text-transform:uppercase}
.card .light-panel{justify-content:center;align-items:center}
.card .light-panel .brand{font-size:15px}
.card .contact{position:absolute;bottom:24px;left:20px;right:20px;font-size:8px;line-height:1.7}
.card .contact .phone{color:var(--orange);font-weight:800;font-size:11px}
.card .inside{padding:24px 16px;gap:10px;justify-content:flex-start}
.card .inside .bar{font-size:8.5px;padding:4px 8px}
.card .inside .list{font-size:8px;line-height:1.6;padding:2px 4px 6px}
.card .inside-right{padding:24px 16px;align-items:flex-start;justify-content:space-between}
.card .inside-right .contact-block{font-size:8px;line-height:1.9}
.card .inside-right .phone{color:var(--orange);font-weight:800;font-size:11px}
.card .inside-right .strip{width:100%;height:6px;background:var(--orange)}
</style>
</head>
<body>
<main class="sheet-set">

  <!-- Full page flyer -->
  <section class="row">
    <div class="item">
      <article class="page full">
        <header class="top"><div class="brand"><span class="brand-mark"></span>HERON VESSELS, INC.</div></header>
        <div class="hero">
          <div class="photo" role="img" aria-label="Photo of metal cutting with bright sparks in a machine shop"></div>
          <h1 class="headline"><span class="white">Fabrication</span><br><span class="orange">and Machining</span></h1>
          <div class="photo-circle" role="img" aria-label="Close-up photo of a welding torch"></div>
        </div>
        <div class="bar cap-bar">Capabilities</div>
        <div class="body">
          <div class="col">
            <div class="block"><p class="section-title">Engineering Support</p><ul class="list"><li>Design review and drafting</li><li>Reverse engineering</li></ul></div>
            <div class="block"><p class="section-title">Vertical Lathes</p><ul class="list"><li>Large diameter turning</li><li>Heavy part capacity</li></ul></div>
            <div class="block"><p class="section-title">Horizontal Lathes</p><ul class="list"><li>Long shaft turning</li><li>Threading and boring</li></ul></div>
            <div class="block"><p class="section-title">Drilling</p><ul class="list"><li>Radial arm drilling</li><li>Deep hole drilling</li></ul></div>
            <div class="block"><p class="section-title">Saw Cutting</p><ul class="list"><li>Bar and plate cutting</li></ul></div>
          </div>
          <div class="col">
            <div class="block"><p class="section-title">Welding</p><ul class="list"><li>MIG, TIG and stick</li><li>Certified welders</li></ul></div>
            <div class="block"><p class="section-title">Repair &amp; Rebuild</p><ul class="list"><li>Field and shop repair</li><li>Component rebuilds</li></ul></div>
            <div class="block"><p class="section-title">Milling</p><ul class="list"><li>CNC vertical milling</li><li>Horizontal boring mill</li></ul></div>
            <div class="block"><p class="section-title">Plate &amp; Sheet</p><ul class="list"><li>Plasma cutting</li><li>Rolling and forming</li></ul></div>
            <div class="block"><p class="section-title">Assembly</p><ul class="list"><li>Fit-up and testing</li></ul></div>
          </div>
          <aside class="side-box">
            <p class="bar">Industries</p>
            <ul class="list"><li>Oil and gas</li><li>Petrochemical</li><li>Power generation</li><li>Marine</li><li>Water treatment</li><li>Mining</li><li>Heavy equipment</li><li>Storage tanks</li></ul>
          </aside>
        </div>
        <footer class="footer"><span class="phone">281-555-0142</span><span>www.heronvesselsinc.example</span></footer>
      </article>
      <p class="size-label">Size 1 (Front)</p>
    </div>

    <div class="item">
      <article class="page full">
        <div class="back-hero photo-cool" role="img" aria-label="Photo of a welder at work with sparks"></div>
        <div class="product">
          <div>
            <h3 class="section-title">Our Product</h3>
            <ul class="arrow-list">
              <li><svg width="8" height="8" viewBox="0 0 8 8"><path d="M1 1l5 3-5 3z" fill="#f26b21"/></svg>Storage tanks</li>
              <li><svg width="8" height="8" viewBox="0 0 8 8"><path d="M1 1l5 3-5 3z" fill="#f26b21"/></svg>Pressure vessels</li>
              <li><svg width="8" height="8" viewBox="0 0 8 8"><path d="M1 1l5 3-5 3z" fill="#f26b21"/></svg>Piping spools</li>
              <li><svg width="8" height="8" viewBox="0 0 8 8"><path d="M1 1l5 3-5 3z" fill="#f26b21"/></svg>Structural steel</li>
              <li><svg width="8" height="8" viewBox="0 0 8 8"><path d="M1 1l5 3-5 3z" fill="#f26b21"/></svg>Machined parts</li>
              <li><svg width="8" height="8" viewBox="0 0 8 8"><path d="M1 1l5 3-5 3z" fill="#f26b21"/></svg>Custom skids</li>
            </ul>
          </div>
          <div class="thumbs">
            <div class="photo" role="img" aria-label="Photo of a fabricated tank"></div>
            <div class="photo-cool" role="img" aria-label="Photo of a machined part"></div>
            <div class="photo-cool" role="img" aria-label="Photo of a lathe in operation"></div>
            <div class="photo" role="img" aria-label="Photo of welded steel assembly"></div>
          </div>
        </div>
        <div class="closing">
          <h2 class="headline"><span class="white">Fabrication</span><br><span class="dark">and Machining</span></h2>
        </div>
        <footer class="footer"><div class="brand on-dark"><span class="brand-mark"></span>HERON VESSELS, INC.</div><span class="phone">281-555-0142</span></footer>
      </article>
      <p class="size-label">Size 1 (Back)</p>
    </div>
  </section>

  <!-- Half page flyer -->
  <section class="row">
    <div class="item">
      <article class="page half">
        <header class="top"><div class="brand"><span class="brand-mark"></span>HERON VESSELS, INC.</div></header>
        <div class="hero">
          <div class="photo" role="img" aria-label="Photo of metal cutting with bright sparks"></div>
          <h1 class="headline"><span class="white">Fabrication</span><br><span class="orange">and Machining</span></h1>
          <div class="photo-circle" role="img" aria-label="Close-up photo of a welding torch"></div>
        </div>
        <div class="bar cap-bar">Capabilities</div>
        <div class="body">
          <div>
            <div class="block"><p class="section-title">Engineering Support</p><ul class="list"><li>Design and drafting</li></ul></div>
            <div class="block"><p class="section-title">Lathes</p><ul class="list"><li>Vertical and horizontal</li></ul></div>
            <div class="block"><p class="section-title">Drilling</p><ul class="list"><li>Radial and deep hole</li></ul></div>
            <div class="block"><p class="section-title">Saw Cutting</p><ul class="list"><li>Bar and plate</li></ul></div>
          </div>
          <div>
            <div class="block"><p class="section-title">Welding</p><ul class="list"><li>Certified welders</li></ul></div>
            <div class="block"><p class="section-title">Repair &amp; Rebuild</p><ul class="list"><li>Field and shop</li></ul></div>
            <div class="block"><p class="section-title">Milling</p><ul class="list"><li>CNC and boring mill</li></ul></div>
            <div class="block"><p class="section-title">Assembly</p><ul class="list"><li>Fit-up and testing</li></ul></div>
          </div>
        </div>
        <footer class="footer"><span class="phone">281-555-0142</span><span>www.heronvesselsinc.example</span></footer>
      </article>
      <p class="size-label">Size 2 (Front)</p>
    </div>

    <div class="item">
      <article class="page half">
        <div class="back-hero photo-cool" role="img" aria-label="Photo of a welder at work with sparks"></div>
        <div class="product">
          <div>
            <h3 class="section-title">Our Product</h3>
            <ul class="arrow-list">
              <li><svg width="8" height="8" viewBox="0 0 8 8"><path d="M1 1l5 3-5 3z" fill="#f26b21"/></svg>Storage tanks</li>
              <li><svg width="8" height="8" viewBox="0 0 8 8"><path d="M1 1l5 3-5 3z" fill="#f26b21"/></svg>Pressure vessels</li>
              <li><svg width="8" height="8" viewBox="0 0 8 8"><path d="M1 1l5 3-5 3z" fill="#f26b21"/></svg>Piping spools</li>
              <li><svg width="8" height="8" viewBox="0 0 8 8"><path d="M1 1l5 3-5 3z" fill="#f26b21"/></svg>Machined parts</li>
            </ul>
          </div>
          <div class="thumbs">
            <div class="photo" role="img" aria-label="Photo of a fabricated tank"></div>
            <div class="photo-cool" role="img" aria-label="Photo of a machined part"></div>
          </div>
        </div>
        <div class="closing">
          <h2 class="headline"><span class="white">Fabrication</span><br><span class="dark">and Machining</span></h2>
        </div>
        <footer class="footer"><div class="brand on-dark"><span class="brand-mark"></span>HERON VESSELS, INC.</div><span class="phone">281-555-0142</span></footer>
      </article>
      <p class="size-label">Size 2 (Back)</p>
    </div>
  </section>

  <!-- Bi-fold business card -->
  <section class="row">
    <div class="item">
      <article class="page card">
        <div class="panel dark-panel">
          <div class="brand on-dark"><span class="brand-mark"></span>HERON VESSELS, INC.</div>
          <p class="tag">Fabrication &amp; Machining</p>
          <div class="contact">
            <p class="phone">281-555-0142</p>
            <p>www.heronvesselsinc.example</p>
          </div>
        </div>
        <div class="panel light-panel">
          <div class="brand"><span class="brand-mark"></span>HERON VESSELS, INC.</div>
        </div>
      </article>
      <p class="size-label">Size 3</p>
    </div>

    <div class="item">
      <article class="page card">
        <div class="panel inside">
          <div><p class="bar">Fabrication</p><ul class="list"><li>Tanks and vessels</li><li>Structural steel</li><li>Certified welding</li></ul></div>
          <div><p class="bar">Machining</p><ul class="list"><li>CNC milling</li><li>Vertical lathes</li><li>Drilling and boring</li></ul></div>
          <div><p class="bar">Services</p><ul class="list"><li>Repair and rebuild</li><li>Engineering support</li></ul></div>
        </div>
        <div class="panel inside-right">
          <div class="brand"><span class="brand-mark"></span>HERON VESSELS, INC.</div>
          <div class="contact-block">
            <p class="phone">281-555-0142</p>
            <p>sales@heronvesselsinc.example</p>
            <p>1200 Foundry Road, Harbor City</p>
            <p>www.heronvesselsinc.example</p>
          </div>
          <div class="strip"></div>
        </div>
      </article>
      <p class="size-label">Business Card</p>
    </div>
  </section>

</main>
</body>
</html>
```